Zorpax.com (Dedicated servers Provider)

We provide dedicated servers for clients around the world. We have created a layout for you. You need to create exactly the design based on these sketches. All text, you can take from our sketches (later we will replace them).

Target Market(s)

Web site owners and web developers

Requirements
Should not have
• The design should not use old-style fonts.

```html
<!DOCTYPE html>
<html lang="en">
<head>
<meta charset="utf-8">
<title>Zorpax.com – Dedicated Servers</title>
<link href="https://fonts.googleapis.com/css2?family=Open+Sans:wght@400;600;700;800&display=swap" rel="stylesheet">
<style>
:root{
  --green:#7ab51d;
  --green-light:#9bcb3c;
  --green-dark:#3f6a10;
  --orange:#f39200;
  --ink:#333;
  --muted:#777;
  --line:#dcdcdc;
  --panel:#f2f2f2;
  --dark:#2a2a2a;
  --darker:#1e1e1e;
  --white:#fff;
}
*{box-sizing:border-box;margin:0;padding:0}
html,body{width:690px;height:1200px;overflow:hidden}
body{font-family:"Open Sans",Arial,sans-serif;color:var(--ink);background:#e9e9e9;font-size:9px;line-height:1.35}
.page{width:690px;height:1200px;position:relative;overflow:hidden}

/* header */
.site-header{height:62px;background:var(--white);display:flex;align-items:center;justify-content:space-between;padding:0 24px}
.brand{display:flex;align-items:center;gap:7px;font-weight:800;font-size:24px;color:var(--ink);letter-spacing:-.5px}
.brand-square{width:20px;height:20px;background:var(--green)}
.header-right{text-align:right}
.call-now{font-size:10px;color:var(--muted)}
.call-now strong{font-size:15px;color:var(--ink);font-weight:800}
.header-buttons{display:flex;gap:6px;margin-top:5px;justify-content:flex-end}
.pill{font-size:8px;color:var(--white);padding:3px 9px;border-radius:3px;font-weight:600}
.pill-green{background:var(--green)}
.pill-orange{background:var(--orange)}

/* nav */
.main-nav{height:24px;background:linear-gradient(#8dc42c,#5f9313);display:flex;align-items:stretch;padding-left:24px}
.main-nav a{color:var(--white);text-decoration:none;font-size:9px;font-weight:600;padding:0 13px;display:flex;align-items:center;border-right:1px solid rgba(255,255,255,.25)}
.main-nav a.active{background:var(--green-dark)}
.main-nav .order-now{margin-left:auto;background:var(--orange);border:0;font-weight:700}
.announcement{height:18px;background:#f8f8f8;border-bottom:1px solid var(--line);font-size:8px;padding:0 24px;display:flex;align-items:center;color:var(--muted)}
.announcement b{color:var(--green-dark);margin-left:4px}

/* hero */
.hero{margin:8px 24px 0;height:150px;background:var(--white);border:1px solid var(--line);position:relative;overflow:hidden}
.hero-title{position:absolute;left:18px;top:10px;font-size:25px;font-weight:700;color:var(--green);line-height:1.2}
.hero-sub{position:absolute;left:20px;top:42px;font-size:9px;color:var(--muted)}
.hero-servers{position:absolute;left:20px;top:58px;width:150px;height:60px;background:linear-gradient(#555,#1c1c1c);border-radius:3px}
.hero-list{position:absolute;left:185px;top:52px;list-style:none;font-size:7.5px;line-height:1.25;color:var(--ink)}
.hero-list li{padding-left:12px;position:relative;margin-bottom:1px}
.hero-list li::before{content:"";position:absolute;left:0;top:2px;width:6px;height:6px;background:var(--green);border-radius:50%}
.hero-btn{position:absolute;left:185px;top:108px;background:var(--green);color:var(--white);font-size:8px;line-height:1.2;font-weight:700;padding:2px 9px;border-radius:3px}
.hero-person{position:absolute;right:40px;top:8px;width:180px;height:118px;background:linear-gradient(160deg,#d8e8f4,#6e9bc4);border-radius:4px}
.hot-offer{position:absolute;right:-30px;top:14px;width:120px;transform:rotate(45deg);background:var(--orange);color:var(--white);font-weight:800;font-size:11px;text-align:center;padding:4px 0}
.hero-bar{position:absolute;left:0;right:0;bottom:0;height:24px;background:linear-gradient(#4b7d14,#2f560a);display:flex;align-items:center;justify-content:space-between;padding:0 14px;color:var(--white)}
.hiring{font-weight:700;font-size:10px;display:flex;align-items:center;gap:6px;line-height:1.1}
.hiring small{display:block;font-size:7px;font-weight:400;opacity:.8}
.hiring-dot{width:14px;height:14px;border-radius:50%;background:var(--green-light)}
.sales{font-size:14px;font-weight:700}
.sales span{color:var(--green-light);font-weight:400}

/* products */
.products{margin:10px 24px 0;height:160px}
.tabs{display:flex;gap:3px;height:20px}
.tab{font-size:8px;padding:4px 14px;background:#dcdcdc;border:1px solid var(--line);border-bottom:0;color:var(--muted)}
.tab.active{background:var(--white);color:var(--ink);font-weight:700}
.cards{background:var(--white);border:1px solid var(--line);height:140px;display:flex;justify-content:space-between;padding:10px 14px}
.card{width:190px;position:relative}
.card h3{font-size:13px;font-weight:700;margin-bottom:5px}
.card-img{position:absolute;left:0;top:26px;width:52px;height:44px;background:linear-gradient(#666,#222);border-radius:3px}
.price{margin-left:60px;font-size:20px;font-weight:800;color:var(--ink);line-height:1}
.price small{font-size:8px;font-weight:400;color:var(--muted)}
.specs{margin-left:60px;font-size:7px;color:var(--muted);margin-top:3px}
.select{margin:28px 0 0 60px;height:12px;border:1px solid var(--line);font-size:7px;padding:0 3px;color:var(--muted)}
.card-foot{position:absolute;left:0;right:0;bottom:0;display:flex;justify-content:space-between;align-items:center}
.card-foot a{font-size:7px;color:var(--ink)}
.order{background:linear-gradient(var(--green-light),var(--green));color:var(--white);font-weight:700;font-size:9px;padding:4px 16px;border-radius:3px}

/* features */
.features{margin:10px 24px 0;height:96px;background:var(--white);border:1px solid var(--line);display:flex;align-items:center;padding:0 14px}
.features-art{width:190px;height:76px;background:radial-gradient(circle,#d9ecb8,#8ec43f);border-radius:40px}
.feature-grid{flex:1;display:grid;grid-template-columns:1fr 1fr;gap:9px 16px;margin-left:24px;list-style:none}
.feature-grid li{display:flex;align-items:center;gap:6px;font-size:8px;font-weight:600}
.tick{width:13px;height:13px;flex:none}

/* testimonial */
.testimonial{margin:10px 24px 0;height:92px;background:var(--white);border:1px solid var(--line);position:relative;text-align:center;padding:14px 52px 0}
.quote-mark{position:absolute;top:4px;font-size:46px;font-weight:800;color:#555;line-height:1}
.quote-mark.open{left:14px}.quote-mark.close{right:14px}
.testimonial p{font-size:10px;font-weight:700;color:var(--ink)}
.testimonial p em{font-style:normal;color:var(--green);font-size:11px}
.testimonial cite{display:block;font-style:normal;font-size:8px;color:var(--muted);margin-top:6px}

/* partners */
.partners{margin:8px 24px 0;height:32px;display:flex;justify-content:space-around;align-items:center}
.partner{width:40px;height:14px;background:#b9b9b9;border-radius:2px}

/* dark section */
.smart-choice{position:absolute;left:0;right:0;top:650px;height:140px;background:var(--dark);padding:10px 24px}
.section-title{text-align:center;font-size:11px;font-weight:700;color:var(--green-light);margin-bottom:10px}
.section-title span{color:var(--white);font-weight:400}
.points{display:grid;grid-template-columns:repeat(3,1fr);gap:12px 20px;list-style:none}
.points li{display:flex;gap:7px;color:#bbb;font-size:7px}
.points b{display:block;color:var(--white);font-size:8px}
.point-icon{width:18px;height:18px;border-radius:50%;background:var(--green);flex:none}

/* stats */
.stats{position:absolute;left:0;right:0;top:790px;height:80px;background:#3a3a3a;padding:8px 24px;border-top:1px solid #444}
.stat-row{display:flex;justify-content:space-around}
.stat{display:flex;align-items:center;gap:6px}
.stat-num{font-size:17px;font-weight:800;color:var(--white)}
.stat-cap{font-size:7px;color:#aaa;width:60px}

/* footer */
.site-footer{position:absolute;left:0;right:0;top:870px;height:290px;background:var(--darker);padding:22px 24px;display:flex;gap:26px;color:#aaa}
.site-footer h4{color:var(--white);font-size:12px;margin-bottom:10px}
.foot-col{font-size:8.5px;line-height:1.55}
.foot-keep{width:170px}
.foot-keep p em{font-style:normal;color:var(--green-light)}
.foot-keep a{display:block;margin-top:14px;color:var(--green-light);font-size:8.5px}
.foot-about{width:220px}
.foot-links{display:grid;grid-template-columns:1fr 1fr;gap:6px;list-style:none}
.foot-links li::before{content:"› ";color:var(--green-light)}
.copyright{margin-top:40px;font-size:7.5px;color:#888}
.foot-info{flex:1}
.phone-box{margin-top:12px;background:#2e2e2e;border:1px solid #444;padding:7px;display:flex;align-items:center;gap:6px;color:var(--white);font-weight:700;font-size:10px}
.news{margin-top:14px}
.news-field{margin-top:5px;height:16px;background:var(--white);border-radius:2px;display:flex;justify-content:flex-end}
.news-field span{background:var(--green);color:var(--white);font-size:7px;padding:2px 8px;border-radius:0 2px 2px 0;font-weight:700}

.bottom-badges{position:absolute;left:0;right:0;top:1160px;height:40px;background:var(--white);display:flex;justify-content:space-around;align-items:center;padding:0 24px}
.badge{width:52px;height:16px;background:#c4c4c4;border-radius:2px}
.badge.wide{width:80px;height:22px;background:#9c9c9c}
</style>
</head>
<body>
<div class="page">

<header class="site-header">
  <div class="brand"><span class="brand-square"></span>Zorpax</div>
  <div class="header-right">
    <div class="call-now">Call Now! <strong>0.800.555.RACK</strong></div>
    <div class="header-buttons">
      <span class="pill pill-green">Sales Department</span>
      <span class="pill pill-orange">Customer Login</span>
      <span class="pill pill-green">Live Chat Online</span>
    </div>
  </div>
</header>

<nav class="main-nav">
  <a class="active">Home</a><a>Dedicated Servers</a><a>Web Hosting</a><a>Limited Sale</a><a>My Account</a><a>Contact</a>
  <a class="order-now">Order Now</a>
</nav>
<div class="announcement">Got an important announcement or a special offer? Tell your customers about it! <b>Read More</b></div>

<section class="hero">
  <h1 class="hero-title">Dedicated Servers</h1>
  <div class="hero-sub">From Swiftrack</div>
  <div class="hero-servers" role="img" aria-label="Rack server units"></div>
  <ul class="hero-list">
    <li>Pure SSD Client for Terminal Server</li>
    <li>Pure Client for Terminal Server</li>
    <li>Pure Mail Terminal Server</li>
    <li>Pure SSD Client for Web Server</li>
    <li>Pure Client for Terminal Server</li>
  </ul>
  <span class="hero-btn">Find Out More</span>
  <div class="hero-person" role="img" aria-label="Businessman holding a globe"></div>
  <div class="hot-offer">Hot Offers</div>
  <div class="hero-bar">
    <div class="hiring"><span class="hiring-dot"></span><div>We Are Hiring<small>Apply Online Today</small></div></div>
    <div class="sales"><span>Call Sales Today</span> 01632 960 123</div>
  </div>
</section>

<section class="products">
  <div class="tabs"><span class="tab active">Dedicated Servers</span><span class="tab">Web Hosting</span><span class="tab">Virtual Private Server</span></div>
  <div class="cards">
    <div class="card">
      <h3>Quadrix Q4 2.4GHz</h3>
      <div class="card-img" role="img" aria-label="Server unit"></div>
      <div class="price">$39.00 <small>/month</small></div>
      <div class="specs">1GB RAM · 80GB HDD<br>1TB Bandwidth</div>
      <div class="select">1 Month – $39.00</div>
      <div class="card-foot"><a>All Dedicated Servers</a><span class="order">ORDER</span></div>
    </div>
    <div class="card">
      <h3>Quadrix Q4 2.4GHz</h3>
      <div class="card-img" role="img" aria-label="Server unit"></div>
      <div class="price">$39.00 <small>/month</small></div>
      <div class="specs">1GB RAM · 80GB HDD<br>1TB Bandwidth</div>
      <div class="select">1 Month – $39.00</div>
      <div class="card-foot"><a>All Dedicated Servers</a><span class="order">ORDER</span></div>
    </div>
    <div class="card">
      <h3>Quadrix Q4 2.4GHz</h3>
      <div class="card-img" role="img" aria-label="Server unit"></div>
      <div class="price">$39.00 <small>/month</small></div>
      <div class="specs">1GB RAM · 80GB HDD<br>1TB Bandwidth</div>
      <div class="select">1 Month – $39.00</div>
      <div class="card-foot"><a>All Dedicated Servers</a><span class="order">ORDER</span></div>
    </div>
  </div>
</section>

<section class="features">
  <div class="features-art" role="img" aria-label="Illustration of people gathered around a circle"></div>
  <ul class="feature-grid">
    <li><svg class="tick" viewBox="0 0 14 14"><circle cx="7" cy="7" r="7" fill="#7ab51d"/><path d="M3.5 7.2l2.3 2.3 4.7-4.8" stroke="#fff" stroke-width="1.8" fill="none"/></svg>100% Network Uptime SLA</li>
    <li><svg class="tick" viewBox="0 0 14 14"><circle cx="7" cy="7" r="7" fill="#7ab51d"/><path d="M3.5 7.2l2.3 2.3 4.7-4.8" stroke="#fff" stroke-width="1.8" fill="none"/></svg>3 SSAE-16 Certified Data Centers</li>
    <li><svg class="tick" viewBox="0 0 14 14"><circle cx="7" cy="7" r="7" fill="#7ab51d"/><path d="M3.5 7.2l2.3 2.3 4.7-4.8" stroke="#fff" stroke-width="1.8" fill="none"/></svg>ISO 9001:2008 Certified</li>
    <li><svg class="tick" viewBox="0 0 14 14"><circle cx="7" cy="7" r="7" fill="#7ab51d"/><path d="M3.5 7.2l2.3 2.3 4.7-4.8" stroke="#fff" stroke-width="1.8" fill="none"/></svg>Coast-to-Coast IP Backbone</li>
    <li><svg class="tick" viewBox="0 0 14 14"><circle cx="7" cy="7" r="7" fill="#7ab51d"/><path d="M3.5 7.2l2.3 2.3 4.7-4.8" stroke="#fff" stroke-width="1.8" fill="none"/></svg>24/7 TTL Technical Support</li>
    <li><svg class="tick" viewBox="0 0 14 14"><circle cx="7" cy="7" r="7" fill="#7ab51d"/><path d="M3.5 7.2l2.3 2.3 4.7-4.8" stroke="#fff" stroke-width="1.8" fill="none"/></svg>Award Winning Since 1999</li>
  </ul>
</section>

<section class="testimonial">
  <span class="quote-mark open">“</span>
  <p><em>The standard chunk of Lorem Ipsum</em> used since the 1500s is reproduced below for those interested. Sections 1.10.32 and 1.10.33 from "de Finibus Bonorum et Malorum" by Tullin are also reproduced in their exact original form</p>
  <cite>www.zorpax-hosting.example</cite>
  <span class="quote-mark close">”</span>
</section>

<div class="partners">
  <span class="partner"></span><span class="partner"></span><span class="partner"></span><span class="partner"></span><span class="partner"></span><span class="partner"></span><span class="partner"></span><span class="partner"></span><span class="partner"></span>
</div>

<section class="smart-choice">
  <h2 class="section-title">NimbleRacks <span>– The Smart Choice For Dedicated Servers</span></h2>
  <ul class="points">
    <li><span class="point-icon"></span><div><b>When an unknown printer took</b>A galley of type and scrambled it to make a type specimen book.</div></li>
    <li><span class="point-icon"></span><div><b>When an unknown printer took</b>A galley of type and scrambled it to make a type specimen book.</div></li>
    <li><span class="point-icon"></span><div><b>When an unknown printer took</b>A galley of type and scrambled it to make a type specimen book.</div></li>
    <li><span class="point-icon"></span><div><b>When an unknown printer took</b>A galley of type and scrambled it to make a type specimen book.</div></li>
    <li><span class="point-icon"></span><div><b>When an unknown printer took</b>A galley of type and scrambled it to make a type specimen book.</div></li>
    <li><span class="point-icon"></span><div><b>When an unknown printer took</b>A galley of type and scrambled it to make a type specimen book.</div></li>
  </ul>
</section>

<section class="stats">
  <h2 class="section-title">NimbleRacks <span>– The Smart Choice For Dedicated Servers</span></h2>
  <div class="stat-row">
    <div class="stat"><span class="stat-num">1,800,000</span><span class="stat-cap">websites hosted across our network</span></div>
    <div class="stat"><span class="stat-num">40,000</span><span class="stat-cap">servers deployed worldwide</span></div>
    <div class="stat"><span class="stat-num">500,000</span><span class="stat-cap">domains under our care</span></div>
    <div class="stat"><span class="stat-num">490,000</span><span class="stat-cap">happy customers served</span></div>
  </div>
</section>

<footer class="site-footer">
  <div class="foot-col foot-keep">
    <h4>Keep it Simple</h4>
    <p><em>The standard chunk of Lorem Ipsum</em> used since the 1500s is reproduced below for those interested. Sections 1.10.32 and 1.10.33 from "de Finibus Bonorum et Malorum"...</p>
    <a>Learn more about Nimble Services</a>
  </div>
  <div class="foot-col foot-about">
    <h4>About Nimble Services</h4>
    <ul class="foot-links">
      <li>About Us</li><li>Careers</li><li>Contact Us</li><li>Other Services</li><li>Terms &amp; Conditions</li><li>Sitemap</li><li>Privacy Policy</li><li>Support</li>
    </ul>
    <p class="copyright">Copyright © 2012 Zorpax.com. All Rights Reserved.<br>Powered by: Nimble web development</p>
  </div>
  <div class="foot-col foot-info">
    <h4>Information</h4>
    <p>Contact us for your dedicated server needs today. Our sales team is ready to help you choose.</p>
    <div class="phone-box">
      <svg width="14" height="14" viewBox="0 0 14 14"><circle cx="7" cy="7" r="7" fill="#7ab51d"/><path d="M4.5 3.5l1.6 0.2 0.5 1.8-1 0.7c.6 1.3 1.5 2.2 2.8 2.8l.7-1 1.8.5.2 1.6c-3.6.5-7.1-3-6.6-6.6z" fill="#fff"/></svg>
      +44 (0) 1632 960 456
    </div>
    <div class="news">Subscribe to our Newsletter
      <div class="news-field"><span>Subscribe</span></div>
    </div>
  </div>
</footer>

<div class="bottom-badges">
  <span class="badge"></span><span class="badge"></span><span class="badge"></span><span class="badge"></span><span class="badge"></span><span class="badge wide"></span><span class="badge"></span>
</div>

</div>
</body>
</html>
```